Brinevale Yacht Management Full Page Ad Flyer

Yacht Management Package also includes the following periodic Monthly services:

Monthly full vessel systems checklist inspections
Diver For Hull Cleaning And Inspection Of Props, Shafts, and Zincs
Interior/Exterior Detailing and scheduled washdowns
Manage Haulout
Pump-out Services
On-call Captain and Crew Services
Updates

Need more time to provide more content to designers and the printing press template file.

Target Market(s)

Vessel owners, motor yachts, sailboats from 25 feet in length up to 125 feet in length. We do not do cruise ships or yachts larger than 125 feet. Someone who has their boat docked at their house or a local marina. We also offer mobile on-site services.

```html
<!DOCTYPE html>
<html lang="en">
<head>
<meta charset="utf-8">
<title>Brinevale Yacht Management – Yacht Management Package</title>
<link rel="stylesheet" href="https://fonts.googleapis.com/css2?family=Montserrat:wght@700;800&family=Poppins:wght@400;500&display=swap">
<style>
  :root {
    --ocean-blue: #1d5aa6;
    --brand-blue: #1f5fab;
    --teal: #5fbfc0;
    --mist: #b9e2e3;
    --white: #ffffff;
    --sky-top: #7fb7e0;
    --sky-low: #d6e8f3;
    --sea-top: #2d6fb3;
    --sea-deep: #123f86;
  }
  * { margin: 0; padding: 0; box-sizing: border-box; }
  html, body { width: 848px; height: 1200px; overflow: hidden; background: var(--white); }
  .flyer {
    position: relative;
    width: 848px;
    height: 1200px;
    overflow: hidden;
    background: var(--ocean-blue);
    font-family: "Poppins", Arial, sans-serif;
    color: var(--white);
  }
  .waves { position: absolute; inset: 0; width: 848px; height: 1200px; }
  .brand-tab {
    position: absolute;
    top: 0; right: 0;
    width: 224px; height: 85px;
    background: var(--white);
    border-bottom-left-radius: 40px;
    display: flex;
    flex-direction: column;
    align-items: center;
    justify-content: center;
    padding-left: 12px;
  }
  .brand-name {
    font-family: "Montserrat", Arial, sans-serif;
    font-weight: 700;
    font-size: 22px;
    letter-spacing: 2px;
    color: var(--brand-blue);
    line-height: 1;
    margin-top: 10px;
  }
  .brand-tagline {
    font-family: "Montserrat", Arial, sans-serif;
    font-weight: 700;
    font-size: 6.5px;
    letter-spacing: 2.4px;
    color: var(--brand-blue);
    margin-top: 5px;
  }
  .headline {
    position: absolute;
    left: 38px;
    top: 108px;
    font-family: "Montserrat", Arial, sans-serif;
    font-weight: 800;
    line-height: 1;
    text-transform: uppercase;
  }
  .headline .line-small { display: block; font-size: 55px; }
  .headline .line-large { display: block; font-size: 87px; margin-top: 8px; letter-spacing: -0.5px; }
  .headline .line-small + .line-large + .line-small { margin-top: 6px; }
  .service-list {
    position: absolute;
    left: 40px;
    top: 358px;
    width: 620px;
    list-style: none;
    font-size: 21px;
    line-height: 1.15;
  }
  .service-list li {
    position: relative;
    padding-left: 16px;
    margin-bottom: 20px;
  }
  .service-list li::before {
    content: "";
    position: absolute;
    left: 0; top: 10px;
    width: 9px; height: 9px;
    border-radius: 50%;
    background: var(--white);
  }
  .service-list .narrow { width: 330px; }
  .contact-bar {
    position: absolute;
    left: 0; right: 0;
    bottom: 14px;
    display: flex;
    justify-content: space-around;
    padding: 0 80px 0 90px;
    font-size: 15px;
  }
  .contact-item { display: flex; align-items: center; gap: 6px; }
  .contact-icon { width: 20px; height: 20px; flex: none; }
</style>
</head>
<body>
<div class="flyer">
  <svg class="waves" viewBox="0 0 848 1200" aria-hidden="false">
    <defs>
      <linearGradient id="yacht-photo-fill" x1="0" y1="0" x2="0" y2="1">
        <stop offset="0" stop-color="var(--sky-top)"/>
        <stop offset="0.35" stop-color="var(--sky-low)"/>
        <stop offset="0.5" stop-color="var(--white)"/>
        <stop offset="0.62" stop-color="var(--sea-top)"/>
        <stop offset="1" stop-color="var(--sea-deep)"/>
      </linearGradient>
    </defs>
    <path class="wave-teal" fill="var(--teal)" d="M0 990 C 190 820, 400 720, 540 630 C 650 560, 740 545, 848 560 V1200 H0 Z"/>
    <path class="wave-mist" fill="var(--mist)" d="M0 860 C 190 800, 380 780, 540 715 C 660 665, 760 668, 848 690 V1200 H0 Z"/>
    <path class="wave-white" fill="var(--white)" d="M0 945 C 190 905, 370 830, 520 770 C 650 718, 760 720, 848 728 V1200 H0 Z"/>
    <path class="yacht-photo" role="img" aria-label="Photo of a white motor yacht with crew on deck cruising across a blue sea under a clear sky" fill="url(#yacht-photo-fill)" d="M0 985 C 190 955, 360 860, 520 795 C 650 742, 760 744, 848 752 V1200 H0 Z"/>
  </svg>

  <div class="brand-tab">
    <span class="brand-name">BRINEVALE</span>
    <span class="brand-tagline">YACHT MANAGEMENT</span>
  </div>

  <h1 class="headline">
    <span class="line-small">Yacht</span>
    <span class="line-large">Management</span>
    <span class="line-small">Package</span>
  </h1>

  <ul class="service-list">
    <li>Monthly full vessel systems checklist inspections</li>
    <li>Diver For Hull Cleaning And Inspection Of Props,<br>Shafts, and Zincs</li>
    <li>Interior/Exterior Detailing and scheduled washdowns</li>
    <li>Manage Haulout</li>
    <li>Pump-out Services</li>
    <li class="narrow">On-call Captain and Crew Services</li>
  </ul>

  <footer class="contact-bar">
    <span class="contact-item">
      <svg class="contact-icon" viewBox="0 0 20 20"><circle cx="10" cy="10" r="10" fill="var(--white)"/><path d="M6.5 5.5 L8.3 5.2 L9.2 7.6 L8 8.5 C8.6 9.9 9.8 11.1 11.3 11.8 L12.2 10.6 L14.6 11.5 L14.3 13.3 C10 13.8 5.9 9.8 6.5 5.5 Z" fill="var(--ocean-blue)"/></svg>
      555-0142-880
    </span>
    <span class="contact-item">
      <svg class="contact-icon" viewBox="0 0 20 20"><circle cx="10" cy="10" r="10" fill="var(--white)"/><rect x="5" y="6.5" width="10" height="7" rx="1" fill="none" stroke="var(--ocean-blue)" stroke-width="1.4"/><path d="M5.4 7 L10 10.6 L14.6 7" fill="none" stroke="var(--ocean-blue)" stroke-width="1.4"/></svg>
      hello@brinevaleyachts.com
    </span>
    <span class="contact-item">
      <svg class="contact-icon" viewBox="0 0 20 20"><circle cx="10" cy="10" r="10" fill="var(--white)"/><circle cx="10" cy="10" r="5" fill="none" stroke="var(--ocean-blue)" stroke-width="1.3"/><ellipse cx="10" cy="10" rx="2.2" ry="5" fill="none" stroke="var(--ocean-blue)" stroke-width="1.1"/><path d="M5 10 H15" stroke="var(--ocean-blue)" stroke-width="1.1"/></svg>
      brinevaleyachts.com
    </span>
  </footer>
</div>
</body>
</html>
```